Harbor Nightclub

Nightclub flyer., digital single sided, for KV and PX. I included samples of some previous flyers we've used. Sample Info:
HARBOR
FRIDAYS
FRI MAY 1 2020
DJ VORTAN (club floor)
DJ RUZO & DJ TAV (residents on the lounge floor)
4217 Marlow Avenue Sacramento
www.harborvenuehall.example for list/VIP inquiries

Target Market(s)

Upscale top 40 crowd but want some cool and artsy like the examples included.

Font styles to use
Sans Serif

Requirements
Must have
• Harbor Logo
Nice to have
• Would be nice if the flyer can be incorporated later with DJ photos (sometimes we will add dj photos to pixagram etc). Would like a big city type of feel.
Should not have
• Nothing too sexual.

```html
<!DOCTYPE html>
<html lang="en">
<head>
<meta charset="utf-8">
<title>Harbor Nightclub – Friday 01 May 2020</title>
<link rel="stylesheet" href="https://fonts.googleapis.com/css2?family=Montserrat:wght@400;600;700;800&display=swap">
<style>
  :root {
    --pink: #e2337c;
    --magenta: #b8318a;
    --violet: #5a2a8e;
    --navy: #120f38;
    --night: #05061a;
    --white: #ffffff;
    --silver: #d9dbe4;
    --gold: #e7c23c;
    --gold-soft: #c9c46a;
    --green: #52d67e;
    --green-deep: #2f9e5a;
  }
  html, body {
    margin: 0;
    padding: 0;
    overflow: hidden;
    background: var(--night);
  }
  .flyer {
    position: relative;
    width: 856px;
    height: 1200px;
    overflow: hidden;
    font-family: "Montserrat", sans-serif;
    color: var(--white);
    background: linear-gradient(180deg, var(--pink) 0%, var(--magenta) 28%, var(--violet) 52%, var(--navy) 75%, var(--night) 100%);
  }
  .city-backdrop {
    position: absolute;
    inset: 0;
    background:
      radial-gradient(ellipse at 20% 55%, rgba(90, 80, 230, 0.45) 0%, rgba(90, 80, 230, 0) 45%),
      radial-gradient(ellipse at 90% 60%, rgba(120, 90, 240, 0.45) 0%, rgba(120, 90, 240, 0) 40%),
      linear-gradient(180deg, rgba(255, 255, 255, 0) 20%, rgba(60, 30, 90, 0.35) 45%, rgba(0, 0, 0, 0) 100%);
  }
  .brand {
    position: absolute;
    top: 38px;
    left: 0;
    width: 100%;
    text-align: center;
  }
  .brand-mark {
    display: block;
    width: 116px;
    height: 116px;
    margin: 0 auto;
    border-radius: 50%;
    background: var(--gold-soft);
  }
  .brand-name {
    margin: 32px 0 0;
    font-size: 60px;
    font-weight: 400;
    letter-spacing: 4px;
    line-height: 1;
    color: var(--white);
  }
  .brand-tag {
    margin: 14px 0 0;
    font-size: 13px;
    font-weight: 400;
    letter-spacing: 4px;
    color: var(--white);
  }
  .feature {
    position: absolute;
    left: 150px;
    top: 270px;
    width: 560px;
    height: 520px;
  }
  .headliner {
    position: absolute;
    top: 790px;
    left: 0;
    width: 100%;
    margin: 0;
    text-align: center;
    font-size: 108px;
    font-weight: 700;
    letter-spacing: 1px;
    line-height: 1;
    background: linear-gradient(90deg, #cfd2de 0%, #e6e2d8 30%, #d9b45a 60%, #a8763a 100%);
    -webkit-background-clip: text;
    background-clip: text;
    color: transparent;
  }
  .light-streak {
    position: absolute;
    top: 900px;
    left: 0;
    width: 100%;
    height: 3px;
    background: linear-gradient(90deg, rgba(120, 150, 255, 0) 0%, rgba(170, 190, 255, 0.9) 50%, rgba(120, 150, 255, 0) 100%);
  }
  .residents {
    position: absolute;
    top: 918px;
    left: 0;
    width: 100%;
    margin: 0;
    text-align: center;
    font-size: 50px;
    font-weight: 700;
    color: var(--silver);
    line-height: 1;
  }
  .date {
    position: absolute;
    top: 990px;
    left: 0;
    width: 100%;
    margin: 0;
    text-align: center;
    font-size: 58px;
    font-weight: 700;
    line-height: 1;
    background: linear-gradient(180deg, var(--green) 0%, var(--green-deep) 100%);
    -webkit-background-clip: text;
    background-clip: text;
    color: transparent;
  }
  .address {
    position: absolute;
    top: 1080px;
    left: 0;
    width: 100%;
    margin: 0;
    text-align: center;
    font-size: 22px;
    font-weight: 600;
    letter-spacing: 5px;
    color: var(--white);
  }
  .inquiries {
    position: absolute;
    top: 1132px;
    left: 0;
    width: 100%;
    margin: 0;
    text-align: center;
    font-size: 21px;
    font-weight: 400;
    letter-spacing: 2.5px;
    color: var(--gold-soft);
  }
</style>
</head>
<body>
  <main class="flyer">
    <div class="city-backdrop" role="img" aria-label="Night city skyline in pink and violet haze with a dancing crowd and blue bokeh lights"></div>

    <header class="brand">
      <span class="brand-mark"></span>
      <h1 class="brand-name">HARBOR</h1>
      <p class="brand-tag">NIGHTCLUB + LOUNGE</p>
    </header>

    <svg class="feature" viewBox="0 0 560 520" aria-hidden="false">
      <defs>
        <linearGradient id="dj-photo-tone" x1="0" y1="0" x2="0" y2="1">
          <stop offset="0" stop-color="#6a3f7a"/>
          <stop offset="0.5" stop-color="#2a1d3a"/>
          <stop offset="1" stop-color="#141020"/>
        </linearGradient>
      </defs>
      <!-- gold offset frame -->
      <polygon points="262,30 505,260 262,490 20,260" fill="none" stroke="var(--gold)" stroke-width="2"/>
      <polygon points="140,150 60,230 60,260 150,170" fill="var(--gold)" opacity="0.85"/>
      <polygon points="500,250 420,330 450,330 520,265" fill="var(--gold)" opacity="0.85"/>
      <!-- featured DJ photo area -->
      <polygon role="img" aria-label="Featured DJ photo: performer in beanie and sunglasses singing into a microphone, headphones around neck"
               points="262,10 500,248 262,486 24,248" fill="url(#dj-photo-tone)"/>
      <!-- silver inner frame -->
      <polygon points="262,68 446,250 262,434 78,250" fill="none" stroke="var(--silver)" stroke-width="9"/>
      <line x1="380" y1="150" x2="560" y2="10" stroke="var(--silver)" stroke-width="1.5" opacity="0.7"/>
      <line x1="120" y1="500" x2="220" y2="420" stroke="var(--silver)" stroke-width="1.5" opacity="0.6"/>
    </svg>

    <h2 class="headliner">DJ VORTAN</h2>
    <div class="light-streak"></div>
    <p class="residents">DJ RUZO &amp; TAV</p>
    <p class="date">FRIDAY | 01 MAY 2020</p>
    <p class="address">4217 MARLOW AVENUE SACRAMENTO</p>
    <p class="inquiries">HARBORVENUEHALL.EXAMPLE FOR LIST/VIP INQUIRIES</p>
  </main>
</body>
</html>
```